Looking for updated Letterhead and Compliments Slips to go with our new updated logo. This stationary will be used for letters to suppliers and customers so needs to be practical while also quite classic.

We are an engineering company so needs to be clean and precise

Target Market(s)

SME'S and large automotive customers

Industry/Entity Type

Automotive

Font styles to use
Sans Serif

Colors
85acd3
0356a4
0792cd
33a6d7
85abd2
ffffff

Requirements
Must have
• Address details as below
• KT Fabrications Limited
• Marbury Close
• Ashbury
• Westmere
• DN47 3XP, UK
• Telephone: +44 (0)1632 960418
• Fax: +44 (0)1632 960735
• Email: sales@ktfabrications.example
• Web: www.ktfabrications.example
Nice to have
• Nice to have some element of being a British Manufacturer

```html
<!DOCTYPE html>
<html lang="en">
<head>
<meta charset="utf-8">
<title>KT Fabrications – Letterhead and Compliments Slip</title>
<link href="https://fonts.googleapis.com/css2?family=Arimo:wght@400;700&family=Crimson+Text:ital@1&display=swap" rel="stylesheet">
<style>
  :root {
    --backdrop: #e6e6e6;
    --paper: #ffffff;
    --ink: #3a3a3a;
    --ink-soft: #555555;
    --brand-navy: #0356a4;
    --brand-sky: #85acd3;
    --brand-cyan: #0792cd;
    --script-ink: #222222;
  }
  * { box-sizing: border-box; margin: 0; padding: 0; }
  html, body { width: 1200px; height: 717px; overflow: hidden; }
  body {
    position: relative;
    background: var(--backdrop);
    font-family: "Arimo", Arial, sans-serif;
    color: var(--ink);
  }
  .sheet {
    position: absolute;
    background: var(--paper);
    box-shadow: 0 2px 10px rgba(0,0,0,0.12);
  }
  .letterhead { left: 239px; top: 72px; width: 409px; height: 583px; }
  .compliments-slip { left: 706px; top: 462px; width: 411px; height: 193px; }

  .brand {
    position: absolute;
    display: flex;
    align-items: center;
    gap: 6px;
    font-family: "Arimo", Arial, sans-serif;
    font-weight: 400;
    color: var(--brand-navy);
    letter-spacing: 2.4px;
    white-space: nowrap;
  }
  .brand-dot {
    width: 8px; height: 8px; border-radius: 50%;
    background: var(--brand-navy);
  }
  .letterhead .brand { left: 0; right: 0; top: 72px; justify-content: center; font-size: 11px; }
  .compliments-slip .brand { left: 28px; top: 63px; font-size: 10px; }

  .recipient {
    position: absolute; left: 62px; top: 169px;
    font-size: 7px; line-height: 8.3px; color: var(--ink); font-style: normal;
  }
  .recipient strong { font-weight: 700; }

  .letter-body {
    position: absolute; left: 62px; top: 227px; width: 286px;
    font-size: 6.7px; line-height: 8.3px; color: var(--ink-soft);
    text-align: justify;
  }
  .letter-body p { margin-bottom: 10px; }
  .letter-body .closing { margin-top: 17px; text-align: left; }

  .signature {
    position: absolute; left: 62px; top: 444px;
    font-size: 7px; line-height: 8.3px;
  }
  .signature strong { font-weight: 700; }

  .contact-footer {
    position: absolute; display: flex;
    font-size: 5.6px; line-height: 7.6px; color: var(--ink);
  }
  .letterhead .contact-footer { left: 61px; top: 532px; }
  .compliments-slip .contact-footer { left: 29px; top: 149px; font-size: 5.3px; line-height: 7.2px; }
  .contact-address { display: flex; gap: 4px; width: 80px; }
  .contact-address strong { font-weight: 700; }
  .contact-lines { list-style: none; }
  .contact-lines li { display: flex; align-items: center; gap: 4px; }
  .icon { width: 6px; height: 6px; flex: none; fill: var(--brand-navy); }
  .contact-address .icon { margin-top: 1px; }

  .slip-heading {
    position: absolute; right: 22px; top: 21px;
    font-family: "Crimson Text", Georgia, serif; font-style: italic;
    font-weight: 400; font-size: 17px; color: var(--script-ink);
  }
</style>
</head>
<body>

<section class="sheet letterhead" aria-label="Letterhead">
  <div class="brand"><span class="brand-dot"></span>KT FABRICATIONS</div>

  <address class="recipient">
    <strong>Mr. Daniel Hart</strong><br>
    Managing Director<br>
    Northfield Capital<br>
    42 Harbour Road<br>
    USA
  </address>

  <div class="letter-body">
    <p>Lorem ipsum dolor sit amet, consectetuer adipiscing elit. Nam cursus. Morbi ut mi. Nullam enim leo, egestas id, condimentum at, laoreet mattis, massa. Sed eleifend nonummy diam. Praesent mauris ante, elementum et, bibendum at, posuere sit amet, nibh. Duis tincidunt lectus quis dui viverra vestibulum.</p>
    <p>Suspendisse vulputate aliquam dui. Nulla elementum dui ut augue. Aliquam vehicula mi at mauris. Maecenas placerat, nisl at consequat rhoncus, sem nunc gravida justo, quis eleifend arcu velit quis lacus. Morbi magna magna, tincidunt a, mattis non, imperdiet vitae, tellus. Sed odio est, auctor ac, sollicitudin in, consequat vitae, orci. Fusce id felis. Vivamus sollicitudin.</p>
    <p>Metus eget eros. Pellentesque habitant morbi tristique senectus et netus et malesuada fames ac turpis egestas. In posuere felis nec tortor. Pellentesque faucibus. Ut accumsan ultricies elit. Maecenas at justo id velit placerat molestie. Donec dictum lectus non odio. Cras a ante vitae enim iaculis aliquam.</p>
    <p>Mauris nunc quam, venenatis nec, euismod sit amet, egestas placerat, est. Pellentesque habitant morbi tristique senectus et netus et malesuada fames ac turpis egestas. Cras id elit. Integer quis urna. Ut ante enim, dapibus malesuada, fringilla eu, condimentum quis, tellus. Aenean porttitor eros vel dolor. Donec convallis pede venenatis nibh. Duis quam. Nam eget.</p>
    <p class="closing">Thank you for being one of our valued customers.</p>
  </div>

  <div class="signature"><strong>Name Here</strong><br>CEO</div>

  <footer class="contact-footer">
    <div class="contact-address">
      <svg class="icon" viewBox="0 0 10 10"><path d="M5 0a3.5 3.5 0 0 0-3.5 3.5C1.5 6 5 10 5 10s3.5-4 3.5-6.5A3.5 3.5 0 0 0 5 0zm0 5a1.5 1.5 0 1 1 0-3 1.5 1.5 0 0 1 0 3z"/></svg>
      <div><strong>KT Fabrications Limited</strong><br>Marbury Close, Ashbury,<br>Westmere<br>DN47 3XP, UK</div>
    </div>
    <ul class="contact-lines">
      <li><svg class="icon" viewBox="0 0 10 10"><path d="M2 0l2 2.5-1.2 1.3a6 6 0 0 0 3.4 3.4L7.5 6 10 8l-1.5 2C4 10 0 6 0 1.5z"/></svg>+44 (0)1632 960418</li>
      <li><svg class="icon" viewBox="0 0 10 10"><rect x="2" y="0" width="6" height="3"/><rect x="0" y="3.5" width="10" height="4.5" rx="1"/><rect x="2" y="7" width="6" height="3"/></svg>+44 (0)1632 960735</li>
      <li><svg class="icon" viewBox="0 0 10 10"><circle cx="5" cy="5" r="5"/><path d="M2.5 3.5h5v3h-5z" fill="#fff"/></svg>sales@ktfabrications.example</li>
      <li><svg class="icon" viewBox="0 0 10 10"><circle cx="5" cy="5" r="5"/><path d="M0 5h10M5 0v10" stroke="#fff" stroke-width="0.8"/></svg>www.ktfabrications.example</li>
    </ul>
  </footer>
</section>

<section class="sheet compliments-slip" aria-label="Compliments slip">
  <div class="brand"><span class="brand-dot"></span>KT FABRICATIONS</div>
  <h2 class="slip-heading">With Compliments</h2>

  <footer class="contact-footer">
    <div class="contact-address">
      <svg class="icon" viewBox="0 0 10 10"><path d="M5 0a3.5 3.5 0 0 0-3.5 3.5C1.5 6 5 10 5 10s3.5-4 3.5-6.5A3.5 3.5 0 0 0 5 0zm0 5a1.5 1.5 0 1 1 0-3 1.5 1.5 0 0 1 0 3z"/></svg>
      <div><strong>KT Fabrications Limited</strong><br>Marbury Close, Ashbury,<br>Westmere<br>DN47 3XP, UK</div>
    </div>
    <ul class="contact-lines">
      <li><svg class="icon" viewBox="0 0 10 10"><path d="M2 0l2 2.5-1.2 1.3a6 6 0 0 0 3.4 3.4L7.5 6 10 8l-1.5 2C4 10 0 6 0 1.5z"/></svg>+44 (0)1632 960418</li>
      <li><svg class="icon" viewBox="0 0 10 10"><rect x="2" y="0" width="6" height="3"/><rect x="0" y="3.5" width="10" height="4.5" rx="1"/><rect x="2" y="7" width="6" height="3"/></svg>+44 (0)1632 960735</li>
      <li><svg class="icon" viewBox="0 0 10 10"><circle cx="5" cy="5" r="5"/><path d="M2.5 3.5h5v3h-5z" fill="#fff"/></svg>sales@ktfabrications.example</li>
      <li><svg class="icon" viewBox="0 0 10 10"><circle cx="5" cy="5" r="5"/><path d="M0 5h10M5 0v10" stroke="#fff" stroke-width="0.8"/></svg>www.ktfabrications.example</li>
    </ul>
  </footer>
</section>

</body>
</html>
```